Criação de Papelaria Profissional para Consultoria de Negócios
A empresa queria:
" Consultoria em planejamento estratégico... marketing... aulas.. palestras.. artigos e livros publicados "

```html
<!DOCTYPE html>
<html lang="pt-BR">
<head>
<meta charset="UTF-8">
<title>Papelaria – Envelopes Leonardo Cardoso</title>
<link href="https://fonts.googleapis.com/css2?family=Cinzel:wght@500&family=Montserrat:wght@400;500&display=swap" rel="stylesheet">
<style>
  :root {
    --bg: #e4e4e2;
    --paper: #ffffff;
    --ink: #2b2b2b;
    --flap: #2e2e2e;
    --accent: #f0531c;
    --muted: #7a7a7a;
    --window: #d6d6d6;
    --watermark: #f0f0f0;
  }
  html, body {
    margin: 0;
    width: 1200px;
    height: 1200px;
    overflow: hidden;
    background: var(--bg);
  }
  .stationery { display: block; width: 1200px; height: 1200px; }
  .paper { fill: var(--paper); }
  .flap { fill: var(--flap); }
  .accent { fill: var(--accent); }
  .ink { fill: var(--ink); }
  .window { fill: none; stroke: var(--window); stroke-width: 2; }
  .brand-name {
    font-family: "Cinzel", serif;
    font-weight: 500;
    font-size: 30px;
    fill: var(--ink);
    letter-spacing: 1px;
  }
  .brand-tagline {
    font-family: "Montserrat", sans-serif;
    font-size: 11px;
    letter-spacing: 6px;
    fill: var(--ink);
  }
  .contact-text {
    font-family: "Montserrat", sans-serif;
    font-size: 8.5px;
    fill: var(--muted);
  }
  .contact-icon { fill: var(--accent); }
  .icon-glyph { fill: none; stroke: #fff; stroke-width: 1.4; stroke-linecap: round; stroke-linejoin: round; }
</style>
</head>
<body>
<svg class="stationery" viewBox="0 0 1200 1200" xmlns="http://www.w3.org/2000/svg">
  <defs>
    <filter id="soft-shadow" x="-10%" y="-10%" width="120%" height="130%">
      <feDropShadow dx="0" dy="4" stdDeviation="5" flood-color="#000" flood-opacity="0.22"/>
    </filter>
  </defs>

  <!-- Envelope front -->
  <g class="envelope envelope-front" filter="url(#soft-shadow)">
    <polygon class="flap" points="283,312 303,203 612,187 913,203 931,312"/>
    <rect class="paper" x="283" y="312" width="648" height="283"/>
    <polygon class="flap" points="283,312 436,312 426,324 283,324"/>
    <polygon class="accent" points="442,314 931,314 931,324 434,324"/>
    <circle cx="795" cy="455" r="110" fill="var(--watermark)"/>
    <g class="brand">
      <circle class="accent" cx="612" cy="398" r="14"/>
      <text class="brand-name" x="612" y="458" text-anchor="middle">Leonardo Cardoso</text>
      <text class="brand-tagline" x="612" y="480" text-anchor="middle">O ESTRATEGISTA</text>
    </g>
    <rect class="window" x="432" y="509" width="341" height="62" rx="2"/>
  </g>

  <!-- Envelope back -->
  <g class="envelope envelope-back" filter="url(#soft-shadow)">
    <rect class="paper" x="278" y="689" width="646" height="314"/>
    <polygon class="flap" points="272,684 930,684 924,704 601,828 278,704"/>
    <polygon class="accent" points="278,988 790,988 782,996 278,996"/>
    <polygon class="flap" points="796,988 924,988 924,996 788,996"/>

    <g class="contact contact-phone">
      <circle class="contact-icon" cx="392" cy="960" r="8"/>
      <path class="icon-glyph" d="M388.5,956.5 q0,6 7,7 l1,-2 -2,-1.5 -1.5,1 q-2,-1 -3,-3 l1,-1.5 -1.5,-2 z"/>
      <text class="contact-text" x="405" y="957">(11) 4000-1200</text>
      <text class="contact-text" x="405" y="968">(11) 9800-3400</text>
    </g>
    <g class="contact contact-mail">
      <circle class="contact-icon" cx="525" cy="960" r="8"/>
      <rect class="icon-glyph" x="520.5" y="956.5" width="9" height="7"/>
      <path class="icon-glyph" d="M520.5,956.5 l4.5,4 4.5,-4"/>
      <text class="contact-text" x="538" y="957">contato@seunome.com</text>
      <text class="contact-text" x="538" y="968">www.seunome.com.br</text>
    </g>
    <g class="contact contact-address">
      <circle class="contact-icon" cx="690" cy="960" r="8"/>
      <path class="icon-glyph" d="M690,965 q-4,-4 -4,-7 a4,4 0 0 1 8,0 q0,3 -4,7 z"/>
      <text class="contact-text" x="703" y="963">Rua das Acácias, 120</text>
    </g>
  </g>
</svg>
</body>
</html>
```